Beacon Advisory Website

I currently have a website www.beaconadvisoryinc.example. We are a IT Consulting Company. Our website will pretty much tell out our services. I am looking to enhance my website and make it look more professional. Looking for very classy and Contemporary look and design for my website.

Industry/Entity Type

It Company

```html
<!DOCTYPE html>
<html lang="en">
<head>
<meta charset="utf-8">
<title>Beacon Advisory</title>
<link href="https://fonts.googleapis.com/css2?family=Open+Sans:ital,wght@0,400;0,600;0,700;1,400;1,600&display=swap" rel="stylesheet">
<style>
:root{
  --blue:#1c5ea8;
  --blue-dark:#17508f;
  --blue-hero:#3f77b3;
  --orange:#f0622a;
  --ink:#222a33;
  --muted:#6b7380;
  --light:#f3f5f8;
  --white:#ffffff;
}
*{box-sizing:border-box;margin:0;padding:0}
html,body{width:1200px;height:3312px;overflow:hidden}
body{font-family:"Open Sans",Arial,sans-serif;color:var(--ink);background:var(--white);position:relative}
a{color:inherit;text-decoration:none}

/* header */
.site-header{position:absolute;top:0;left:0;width:1200px;height:72px;background:var(--white);display:flex;align-items:center;padding:0 120px;z-index:2}
.brand{display:flex;align-items:center;gap:10px;font-weight:700;font-size:17px;color:var(--blue);letter-spacing:.5px;line-height:1.05}
.brand-mark{width:34px;height:34px;background:var(--blue)}
.main-nav{margin-left:auto;display:flex;gap:26px;font-size:12px;font-weight:600;color:var(--ink)}
.main-nav a{padding:26px 0;border-bottom:3px solid transparent}
.main-nav a.active{color:var(--blue);border-color:var(--blue)}
.nav-phone{margin-left:30px;font-size:13px;font-weight:600}

/* hero */
.hero{position:absolute;top:72px;left:0;width:1200px;height:548px;background:linear-gradient(120deg,#5a8dc4 0%,#7ea7d3 45%,#a9c4e2 70%,#6f98c7 100%)}
.hero-content{position:absolute;left:240px;top:36px;width:460px;color:var(--white)}
.hero h1{font-size:38px;font-weight:700;line-height:1.15;letter-spacing:.5px}
.hero p{margin-top:20px;font-size:15px;line-height:1.5;opacity:.95}
.hero-actions{margin-top:28px;display:flex;align-items:center;gap:180px}
.btn{display:inline-block;background:var(--orange);color:var(--white);font-size:14px;font-weight:600;padding:10px 26px}
.link-more{font-size:12px;color:var(--white)}
.hero-thumbs{position:absolute;right:120px;bottom:34px;display:flex;gap:6px}
.hero-thumbs span{width:50px;height:50px;display:block}

/* services */
.services{position:absolute;top:620px;left:0;width:1200px;height:612px;background:var(--white)}
.section-title{font-size:28px;font-weight:700;color:var(--blue);letter-spacing:1px}
.services .section-title{text-align:center;margin-top:60px}
.services .section-title::after{content:"";display:block;width:40px;height:3px;background:var(--blue);margin:10px auto 0}
.service-list{display:flex;justify-content:center;gap:60px;margin-top:40px}
.service{width:260px;text-align:center}
.service-visual{width:180px;height:180px;margin:30px auto 40px;transform:rotate(45deg)}
.service h3{font-size:18px;font-weight:700;margin-bottom:8px}
.service p{font-size:14px;line-height:1.45;color:var(--ink)}
.carousel-arrow{position:absolute;top:280px;width:20px;height:30px}
.carousel-arrow.prev{left:110px}.carousel-arrow.next{right:110px}

/* solution */
.solution{position:absolute;top:1232px;left:0;width:1200px;height:588px}
.solution-panel{position:absolute;left:0;top:0;width:580px;height:588px;background:var(--blue);color:var(--white);padding:200px 120px 0 120px}
.solution-panel h2{font-size:28px;font-weight:700;letter-spacing:1px}
.solution-panel p{margin-top:18px;font-size:13px;line-height:1.55;opacity:.95}
.solution-panel .btn{margin-top:24px;font-size:12px;padding:7px 16px}
.solution-photo{position:absolute;left:580px;top:0;width:620px;height:588px;background:linear-gradient(160deg,#c9ccd2 0%,#8d8f95 40%,#3b3d44 75%,#1f2126 100%)}

/* career */
.career{position:absolute;top:1820px;left:0;width:1200px;height:660px;background:var(--white)}
.career .section-title{position:absolute;left:120px;top:80px}
.profile-photo{position:absolute;left:120px;top:172px;width:400px;height:400px;background:linear-gradient(180deg,#e4e6e9 0%,#cfd2d6 55%,#2a2d33 100%)}
.profile{position:absolute;left:560px;top:172px;width:520px}
.profile h3{font-size:26px;font-style:italic;font-weight:600;color:var(--blue)}
.profile .role{font-size:12px;font-style:italic;color:var(--muted);margin-top:4px}
.profile .email{font-size:12px;font-style:italic;color:var(--muted)}
.profile p{margin-top:18px;font-size:14px;line-height:1.5}
.social-row{display:flex;gap:22px;margin-top:40px}
.social-row span{width:14px;height:14px;border-radius:50%;background:#8a919b}
.team-thumbs{display:flex;gap:8px;margin-top:30px}
.team-thumbs span{width:58px;height:58px;background:var(--blue-hero)}
.team-thumbs span.current{background:linear-gradient(180deg,#dfe2e6,#3a3e45)}

/* contact */
.contact{position:absolute;top:2480px;left:0;width:1200px;height:440px;background:var(--light)}
.contact-info{position:absolute;left:120px;top:70px;width:240px}
.contact h2{font-size:28px;font-weight:700;color:var(--blue);letter-spacing:1px}
.contact h4{font-size:13px;font-weight:600;margin-top:14px}
.contact address{font-style:normal;font-size:12px;line-height:1.55;margin-top:8px}
.contact-map{position:absolute;left:360px;top:0;width:840px;height:440px;background:linear-gradient(135deg,#e9e4d8 0%,#f2efe6 50%,#dfe6d6 100%)}
.map-pin{position:absolute;left:240px;top:160px}

/* footer */
.site-footer{position:absolute;top:2920px;left:0;width:1200px;height:392px;background:var(--blue-dark);color:var(--white);padding:50px 120px 0}
.footer-cols{display:flex;gap:0}
.footer-col{width:180px}
.footer-col h5{font-size:16px;font-weight:600;margin-bottom:14px}
.footer-col li{list-style:none;font-size:12px;line-height:2;opacity:.9}
.newsletter{margin-left:20px;width:260px}
.newsletter h5{font-size:15px;font-weight:600;line-height:1.35}
.newsletter .field{margin-top:16px;width:220px;height:30px;background:var(--white);font-size:11px;color:var(--muted);padding:7px 10px}
.newsletter .btn{margin-top:10px;font-size:12px;padding:6px 16px}
.footer-bottom{position:absolute;left:120px;bottom:36px;display:flex;align-items:center;gap:14px;font-size:14px}
.footer-bottom .icon{width:14px;height:14px;border-radius:50%;background:var(--white);opacity:.85}
.footer-bottom small{margin-left:30px;font-size:11px;opacity:.8}
</style>
</head>
<body>

<header class="site-header">
  <div class="brand"><span class="brand-mark"></span><span>BEACON<br>ADVISORY</span></div>
  <nav class="main-nav">
    <a class="active" href="#">COMPANY</a>
    <a href="#">SERVICES</a>
    <a href="#">SOLUTIONS</a>
    <a href="#">RESOURCES</a>
    <a href="#">CAREER</a>
    <a href="#">CONTACT US</a>
  </nav>
  <span class="nav-phone">+1 (555) 014 2290</span>
</header>

<section class="hero" role="img" aria-label="Blue-toned photo of hands reviewing documents at a desk">
  <div class="hero-content">
    <h1>WECOME TO BEACON<br>ADVISORY</h1>
    <p>Beacon Advisory has certified professional consultants to work with you to help improve the business by providing IT services.</p>
    <div class="hero-actions">
      <a class="btn" href="#">Get Started Now</a>
      <a class="link-more" href="#">Learn more →</a>
    </div>
  </div>
  <div class="hero-thumbs">
    <span style="background:#3c4d63"></span>
    <span style="background:#c9ced6"></span>
    <span style="background:#5b6470"></span>
  </div>
</section>

<section class="services">
  <h2 class="section-title">SERVICES</h2>
  <svg class="carousel-arrow prev" viewBox="0 0 20 30"><path d="M15 3 4 15l11 12" fill="none" stroke="#9aa2ad" stroke-width="3"/></svg>
  <svg class="carousel-arrow next" viewBox="0 0 20 30"><path d="M5 3l11 12L5 27" fill="none" stroke="#9aa2ad" stroke-width="3"/></svg>
  <div class="service-list">
    <article class="service">
      <div class="service-visual" role="img" aria-label="Photo of a person working on a laptop" style="background:linear-gradient(135deg,#dfe3e8,#8a96a6)"></div>
      <h3>Technology</h3>
      <p>Beacon Advisory has certified professional consultants to work with you to help</p>
    </article>
    <article class="service">
      <div class="service-visual" role="img" aria-label="Photo of a business handshake" style="background:linear-gradient(135deg,#e6e8eb,#7e8794)"></div>
      <h3>Offshore Business</h3>
      <p>Beacon Advisory has certified professional consultants to work with you to help</p>
    </article>
    <article class="service">
      <div class="service-visual" role="img" aria-label="Photo of a team meeting around a table" style="background:linear-gradient(135deg,#d9dde3,#6d7888)"></div>
      <h3>Enterprise Integration</h3>
      <p>Beacon Advisory has certified professional consultants to work with you to help</p>
    </article>
  </div>
</section>

<section class="solution">
  <div class="solution-panel">
    <h2>SOLUTION</h2>
    <p>Lorem ipsum dolor sit amet, consectetur adipiscing elit, sed do eiusmod tempor incididunt ut labore et dolore magna aliqua. Lorem ipsum dolor sit amet, consectetur adipiscing elit, sed do eiusmod incididunt ut labore et dolore magna aliqua.</p>
    <a class="btn" href="#">LEARN MORE</a>
  </div>
  <div class="solution-photo" role="img" aria-label="Photo of three business people reviewing a tablet outdoors"></div>
</section>

<section class="career">
  <h2 class="section-title">CAREER</h2>
  <div class="profile-photo" role="img" aria-label="Portrait photo of a consultant in a suit"></div>
  <div class="profile">
    <h3>Marcus Hale</h3>
    <div class="role">Executive Director</div>
    <div class="email">marcus@beaconadvisory.example</div>
    <p>Lorem ipsum dolor sit amet, consectetur adipiscing elit, sed do eiusmod incididunt ut labore et dolore magna aliqua. Lorem ipsum dolor sit amet consectetur adipiscing elit, sed do eiusmod incididunt ut labore et dolore magna aliqua.</p>
    <div class="social-row"><span></span><span></span><span></span></div>
    <div class="team-thumbs"><span class="current"></span><span></span><span></span><span></span></div>
  </div>
</section>

<section class="contact">
  <div class="contact-info">
    <h2>CONTACT US</h2>
    <h4>Head Office</h4>
    <address>120 Harbor Lane<br>Suite 300<br>Easton, NJ 07000<br>Phone: +1 (555) 014 2290</address>
    <h4>Technical Center</h4>
    <address>4500 Ridge Road<br>Suite 110<br>Lakeview, MI 48000</address>
  </div>
  <div class="contact-map" role="img" aria-label="Street map showing the office location">
    <svg class="map-pin" width="40" height="54" viewBox="0 0 40 54"><path d="M20 2C10 2 3 9 3 19c0 13 17 33 17 33s17-20 17-33C37 9 30 2 20 2z" fill="#1c5ea8"/><circle cx="20" cy="19" r="6" fill="#fff"/></svg>
  </div>
</section>

<footer class="site-footer">
  <div class="footer-cols">
    <div class="footer-col"><h5>About us</h5><ul><li>Company</li><li>Services</li><li>Solution</li><li>Resources</li><li>Career</li><li>Contact Us</li></ul></div>
    <div class="footer-col"><h5>Services</h5><ul><li>Technology</li><li>Offshore Business</li><li>Application Development</li><li>Enterprise Integration</li><li>IT Consulting</li></ul></div>
    <div class="footer-col"><h5>Solutions</h5><ul><li>Dashboard</li><li>eWarehousing</li><li>BPM</li></ul></div>
    <div class="footer-col"><h5>Resources</h5><ul><li>Our Process</li><li>Staff Augmentation</li></ul></div>
    <div class="newsletter">
      <h5>Submit your e-mail receive back details within 24 hours</h5>
      <div class="field">your email id</div>
      <a class="btn" href="#">SUBSCRIBE</a>
    </div>
  </div>
  <div class="footer-bottom">
    <span>Follow us</span><span class="icon"></span><span class="icon"></span><span class="icon"></span><span class="icon"></span>
    <small>© 2015</small>
  </div>
</footer>

</body>
</html>
```